MCP phase 1 web design

Meridale Capital Partners Ltd (MCP) is a challenger business to the traditional leasing market. We look for solutions to complex problems involving the funding of capital equipment within an office environment and then build documentation around the solution. We recently created a brief for a logo and successfully completed that assignment. We now need to create our first web site which is simply intended to be informative. To help interested designers we have attached a detailed brief that is broken into three sections. The first explains how we see the site developing over time from something quite straightforward initially to a full transaction capability. Whoever wins this competition will be expected to work with us into the future to help develop the site. Section 2 gives you a view about our likes and dislikes by reviewing some existing sites. Section 3 gives you the structure and content of the site based upon our likes and dislikes. We are by no means committed to the structure and if you believe it can be presented in a better way then please use your design. The text is fixed as content. The images to appear can be anything from photographs to line drawings again entirely at the designers whim. Currently we have a home page plus 5 subsidiary pages. A few things to help you:
1. The logo is fixed and should be amongst the downloads.
2. The colours we have are corporate and should be used.
3. The typeface we use within the business is "Verdana"
Good luck.

```html
<!DOCTYPE html>
<html lang="en">
<head>
<meta charset="utf-8">
<title>Meridale Capital Partners Ltd</title>
<link href="https://fonts.googleapis.com/css2?family=Noto+Sans:wght@400;700&family=Roboto+Condensed:wght@400;700&display=swap" rel="stylesheet">
<style>
  :root {
    --brand-blue: #1d6cb5;
    --brand-blue-dark: #0f5aa6;
    --text: #5a5a5a;
    --nav-text: #4a4a4a;
    --page-bg: #dcdcdc;
    --rule: #d8d8d8;
    --white: #ffffff;
    --footer-bar: #4a4a4a;
  }
  * { box-sizing: border-box; margin: 0; padding: 0; }
  html, body { width: 1200px; height: 726px; overflow: hidden; }
  body {
    background: linear-gradient(90deg, #c9c9c9 0%, #e9e9e9 11%, #e9e9e9 89%, #c9c9c9 100%);
    font-family: "Noto Sans", Verdana, sans-serif;
    color: var(--text);
    letter-spacing: 0.3px;
  }
  .stage { width: 1240px; height: 750px; position: relative; transform: scale(0.967742); transform-origin: 0 0; }
  .site { position: absolute; left: 140px; top: 0; width: 960px; height: 750px; background: var(--page-bg); }

  .site-header { position: absolute; left: 0; top: 0; width: 960px; height: 94px; background: var(--white); border-bottom: 1px solid var(--rule); }
  .brand { position: absolute; left: 12px; top: 30px; display: flex; align-items: center; gap: 10px;
    font-family: "Roboto Condensed", sans-serif; font-weight: 400; color: var(--brand-blue); font-size: 25px; letter-spacing: 0.5px; }
  .brand-mark { width: 14px; height: 14px; background: var(--brand-blue); }
  .header-mail { position: absolute; right: 26px; top: 9px; font-size: 13px; letter-spacing: 0; color: var(--brand-blue); display: flex; align-items: center; gap: 9px; }
  .main-nav { position: absolute; right: 24px; top: 46px; display: flex; font-family: "Roboto Condensed", sans-serif; font-size: 14.5px; letter-spacing: 0.3px; color: var(--nav-text); }
  .main-nav span { padding: 3px 16px; border-left: 1px solid var(--rule); display: flex; align-items: center; gap: 6px; }
  .main-nav span:first-child { border-left: none; }
  .main-nav span:last-child { padding-left: 10px; padding-right: 0; }

  .hero { position: absolute; left: 0; top: 94px; width: 960px; height: 385px; background: var(--white); }
  .hero-photo { position: absolute; left: 0; top: 0; width: 678px; height: 385px;
    background: linear-gradient(165deg, #9c9c9c 0%, #c9ccd0 22%, #eef1f4 42%, #e4edf5 58%, #7fb1d8 80%, #3d85c2 100%); }
  .slider-dots { position: absolute; left: 12px; top: 364px; display: flex; gap: 4px; }
  .slider-dots i { width: 9px; height: 9px; border-radius: 50%; background: #d6d6d6; border: 1px solid #bdbdbd; display: block; }
  .slider-dots i.active { background: var(--brand-blue); border-color: var(--brand-blue); }
  .intro { position: absolute; left: 688px; top: 9px; width: 262px; height: 366px;
    background: linear-gradient(135deg, #cde0ef 0%, #e3eef7 55%, #d4e4f1 100%); padding: 23px 14px 0 20px;
    font-size: 12.4px; line-height: 18px; color: #555; }
  .intro p + p { margin-top: 18px; }
  .calc-btn { position: absolute; left: 24px; top: 292px; width: 212px; height: 40px; border-radius: 20px;
    background: linear-gradient(#2a86d4, var(--brand-blue-dark)); color: var(--white); letter-spacing: 0;
    font-family: "Roboto Condensed", sans-serif; font-size: 14px; display: flex; align-items: center; padding-left: 20px; gap: 16px; }

  .solutions { position: absolute; left: 0; top: 483px; width: 960px; height: 154px; }
  .solution { position: absolute; top: 0; height: 154px; width: 317px; background: var(--white); }
  .solution:nth-child(1) { left: 0; }
  .solution:nth-child(2) { left: 321px; }
  .solution:nth-child(3) { left: 643px; }
  .solution-photo { position: absolute; left: 24px; top: 27px; width: 92px; height: 92px; border-radius: 6px; }
  .solution h2 { position: absolute; left: 141px; top: 23px; width: 150px; font-family: "Roboto Condensed", sans-serif;
    font-weight: 700; font-size: 18px; line-height: 20px; letter-spacing: 0.2px; color: var(--brand-blue); }
  .solution p { position: absolute; left: 141px; top: 72px; width: 155px; font-size: 12.4px; line-height: 17px; color: #666; }
  .solution:nth-child(2) .solution-photo { left: 22px; }
  .solution:nth-child(2) h2 { left: 147px; width: 130px; }
  .solution:nth-child(2) p { left: 147px; width: 160px; }
  .solution:nth-child(3) .solution-photo { left: 25px; }
  .solution:nth-child(3) h2 { left: 149px; width: 165px; }
  .solution:nth-child(3) p { left: 149px; top: 53px; width: 145px; }

  .site-footer { position: absolute; left: 0; top: 641px; width: 960px; height: 102px; background: var(--white); font-size: 11.5px; line-height: 20px; color: #555; }
  .address { position: absolute; left: 18px; top: 37px; display: flex; gap: 12px; }
  .legal { position: absolute; right: 15px; top: 36px; text-align: right; }
  .footer-bar { position: absolute; left: 0; top: 743px; width: 960px; height: 7px; background: var(--footer-bar); }
</style>
</head>
<body>
<div class="stage">
  <div class="site">
    <header class="site-header">
      <div class="brand"><span class="brand-mark"></span>Meridale Capital Partners Ltd</div>
      <div class="header-mail">
        <svg width="17" height="12" viewBox="0 0 17 12"><rect width="17" height="12" fill="#555"/><path d="M0 0 L8.5 7 L17 0" fill="none" stroke="#fff" stroke-width="1.2"/></svg>
        info@meridalecp.co.uk
      </div>
      <nav class="main-nav">
        <span>WHY MERIDALE</span>
        <span>SOLUTIONS <svg width="9" height="6" viewBox="0 0 9 6"><path d="M1 1 L4.5 4.5 L8 1" fill="none" stroke="#666" stroke-width="1.2"/></svg></span>
        <span>CONTACT US</span>
      </nav>
    </header>

    <section class="hero">
      <div class="hero-photo" role="img" aria-label="Photograph of hands holding pens over printed financial bar and pie charts"></div>
      <div class="slider-dots"><i></i><i class="active"></i><i></i><i></i></div>
      <div class="intro">
        <p>We provide "Sales Aid Finance" through <b>MERIDALE</b> financial &amp; contract solutions. Specialising in the Print &amp; Technology markets, we offer Value Added Resellers (VARs) a range of innovative, cost effective, value added contract &amp; finance options to enhance their sales.</p>
        <p>Our solutions are fully financed &amp; we are totally independent from any VAR, technology provider or traditional finance house.</p>
        <div class="calc-btn">
          <svg width="19" height="25" viewBox="0 0 19 25"><rect x="0" y="0" width="19" height="25" rx="2" fill="#fff"/><rect x="3" y="3" width="13" height="5" fill="#1569b8"/><g fill="#1569b8"><rect x="3" y="11" width="3" height="3"/><rect x="8" y="11" width="3" height="3"/><rect x="13" y="11" width="3" height="3"/><rect x="3" y="16" width="3" height="3"/><rect x="8" y="16" width="3" height="3"/><rect x="13" y="16" width="3" height="3"/><rect x="3" y="20" width="3" height="2"/><rect x="8" y="20" width="3" height="2"/><rect x="13" y="20" width="3" height="2"/></g></svg>
          COST CALCULATOR
        </div>
      </div>
    </section>

    <section class="solutions">
      <article class="solution">
        <div class="solution-photo" role="img" aria-label="Photograph of a hand using a tablet showing a chart" style="background:linear-gradient(150deg,#f0f0f0 0%,#c9c2bb 30%,#3a4a55 60%,#0f1a22 85%,#2aa0c8 100%);"></div>
        <h2>Managed Services Solutions</h2>
        <p>MCP's Managed Services solutions offer all the flexibility...</p>
      </article>
      <article class="solution">
        <div class="solution-photo" role="img" aria-label="Photograph of a team meeting around a table seen from above" style="background:radial-gradient(circle at 50% 45%,#f5d9a8 0%,#e09a4c 40%,#a85a24 70%,#3a2216 100%);"></div>
        <h2>Public Sector Solutions</h2>
        <p>Most public sector bodies increasingly require contract flexibility...</p>
      </article>
      <article class="solution">
        <div class="solution-photo" role="img" aria-label="Photograph of a teacher presenting at an interactive whiteboard to a class" style="background:linear-gradient(170deg,#f4f4f4 0%,#dfe6ec 40%,#6fb6dc 62%,#8a7a5a 80%,#3e4650 100%);"></div>
        <h2>Education Solutions</h2>
        <p>Schools, academies &amp; most education providers ask their technology suppliers...</p>
      </article>
    </section>

    <footer class="site-footer">
      <div class="address">
        <svg width="11" height="16" viewBox="0 0 11 16"><path d="M5.5 0 C2.5 0 0 2.4 0 5.4 C0 9.5 5.5 16 5.5 16 C5.5 16 11 9.5 11 5.4 C11 2.4 8.5 0 5.5 0 Z" fill="#666"/><circle cx="5.5" cy="5.4" r="2" fill="#fff"/></svg>
        <div>Fenwick House, 48 Aldgate Row,<br>London, EC3N 2QT</div>
      </div>
      <div class="legal">Copyright © MCP 2014. All rights reserved.<br>Meridale Capital Partners Ltd. is registered in England.</div>
    </footer>
    <div class="footer-bar"></div>
  </div>
</div>
</body>
</html>
```